Create a business promotion flyer to leave in customer mailboxes. We are a bulk petroleum supplier, servicing any industry that requires diesel. Base in griffith NSW, servicing griffith area and surrounds.

Business Name - Terra Petro
Fuel@terrapetro-example.com.au
Marco - 0400 000 001 mtorrisi@terrapetro-example.com.au
Liam - 0400 000 002 lharcourt@terrapetro-example.com.au
Peter - 0400 000 003 pwinslow@terrapetro-example.com.au
Office 02 5550 0100

Bulk Fuel deliveries.
Oils & lubricants
Local Family owned business

```html
<!DOCTYPE html>
<html lang="en">
<head>
<meta charset="utf-8">
<title>Terra Petro – Bulk Fuel Flyer</title>
<link rel="stylesheet" href="https://fonts.googleapis.com/css2?family=Montserrat:wght@500;600;700&family=Roboto+Condensed:wght@400;500;700&display=swap">
<style>
  :root {
    --red: #d71920;
    --ink: #1b1b1b;
    --charcoal: #2b2b2b;
    --panel-dark: #141211;
    --paper: #ffffff;
    --soft: #f4f4f4;
    --page-bg: #ececec;
  }
  * { margin: 0; padding: 0; box-sizing: border-box; }
  html, body { width: 933px; height: 1200px; overflow: hidden; background: var(--page-bg); }
  .flyer {
    position: absolute; left: 52px; top: 20px;
    width: 828px; height: 1160px;
    background: var(--paper); overflow: hidden;
    font-family: "Montserrat", sans-serif; color: var(--ink);
  }
  .hero-photo {
    position: absolute; left: 0; top: 0; width: 828px; height: 340px;
    background: linear-gradient(180deg, #3c3f58 0%, #7a6a78 35%, #e0a676 60%, #8b8a86 75%, #5b5a58 100%);
  }
  .hero-swoosh { position: absolute; left: 0; top: 200px; width: 828px; height: 170px; }
  .brand-badge {
    position: absolute; left: 33px; top: 16px; width: 276px; height: 276px;
    border-radius: 50%; background: var(--paper);
    box-shadow: 0 4px 14px rgba(0,0,0,.35);
    display: flex; align-items: center; justify-content: center;
  }
  .brand-name { font-weight: 600; font-size: 40px; color: var(--red); letter-spacing: -.5px; }
  .intro {
    position: absolute; left: 0; top: 324px; width: 828px;
    text-align: center; font-weight: 500; font-size: 20.5px; line-height: 30px;
  }
  .intro .accent { color: var(--red); }
  .coverage {
    position: absolute; left: 14px; top: 428px; width: 401px; height: 373px;
    background: radial-gradient(circle at 40% 40%, #2a2522, var(--panel-dark));
    color: #fff; font-family: "Roboto Condensed", sans-serif;
  }
  .coverage-map {
    position: absolute; left: 74px; top: 6px; width: 292px; height: 204px;
    background: linear-gradient(135deg, #0b0b0b, #181414);
    border: 1px solid #7a1a1a;
  }
  .town {
    position: absolute; font-size: 17px; text-align: right; line-height: 1;
    transform: translateY(-50%);
  }
  .town::after {
    content: ""; position: absolute; right: -17px; top: 50%;
    width: 9px; height: 9px; border-radius: 50%; background: var(--red);
    transform: translateY(-50%);
  }
  .coverage-title {
    position: absolute; left: 0; top: 216px; width: 401px; text-align: center;
    font-weight: 500; font-size: 27px; line-height: 29.5px; letter-spacing: .2px;
  }
  .coverage-note {
    position: absolute; left: 0; top: 313px; width: 401px; text-align: center;
    font-family: "Montserrat", sans-serif; font-size: 13.5px; line-height: 17px;
  }
  .contacts {
    position: absolute; left: 443px; top: 428px; width: 385px; height: 373px;
    background: linear-gradient(90deg, var(--soft), #fafafa);
  }
  .contact { position: absolute; left: 0; width: 385px; height: 60px; }
  .contact-icon { position: absolute; left: 7px; top: 4px; width: 52px; height: 52px; }
  .contact-title {
    position: absolute; left: 86px; top: 2px; color: var(--red);
    font-weight: 700; font-size: 23px; line-height: 28px; white-space: nowrap;
  }
  .contact-email {
    position: absolute; left: 86px; top: 33px; font-weight: 500;
    font-size: 14px; line-height: 18px; white-space: nowrap;
  }
  .yard-photo {
    position: absolute; left: 0; top: 811px; width: 828px; height: 254px;
    background: linear-gradient(90deg, #5d6b55 0%, #b3262a 25%, #c8282c 55%, #9a2a2a 75%, #a9b7c4 100%);
  }
  .services {
    position: absolute; left: 0; top: 1065px; width: 828px; height: 95px;
  }
  .service { position: absolute; top: 0; height: 95px; }
  .service svg { position: absolute; top: 20px; }
  .service-label {
    position: absolute; top: 31px; white-space: nowrap;
    font-family: "Roboto Condensed", sans-serif; font-weight: 700;
    font-size: 19px; line-height: 25px; color: var(--ink);
  }
</style>
</head>
<body>
<main class="flyer">
  <div class="hero-photo" role="img" aria-label="White fuel tanker truck on a road under a sunset sky"></div>
  <svg class="hero-swoosh" viewBox="0 0 828 170" preserveAspectRatio="none" aria-hidden="true">
    <path d="M0 5 C 200 20, 450 70, 828 100 L828 170 L0 170 Z" fill="var(--red)"/>
    <path d="M0 63 C 250 50, 550 55, 828 140 L828 170 L0 170 Z" fill="var(--charcoal)"/>
    <path d="M0 121 C 250 75, 600 75, 828 162 L828 170 L0 170 Z" fill="var(--paper)"/>
  </svg>
  <div class="brand-badge"><span class="brand-name">Terra Petro</span></div>

  <p class="intro">
    <span class="accent">Terra Petro</span> We are a bulk petroleum supplier,<br>
    servicing any industry that requires diesel.<br>
    Based in Griffith <span class="accent">NSW</span>, servicing Griffith area and surrounds.
  </p>

  <section class="coverage">
    <div class="coverage-map" role="img" aria-label="Outline map of New South Wales"></div>
    <span class="town" style="right:146px;top:37px">Griffith</span>
    <span class="town" style="right:155px;top:64px">Leeton</span>
    <span class="town" style="right:162px;top:91px">Narrandera</span>
    <span class="town" style="right:167px;top:118px">Wagga Wagga</span>
    <span class="town" style="right:189px;top:144px">Yoogali</span>
    <span class="town" style="right:130px;top:166px">Hanwood</span>
    <span class="town" style="right:138px;top:191px">Yenda</span>
    <h2 class="coverage-title">AVAILABLE ACROSS<br>GRIFFITH AND<br>SURROUNDING AREAS</h2>
    <p class="coverage-note">Local expertise and resources<br>ready to service<br>across the region.</p>
  </section>

  <section class="contacts">
    <div class="contact" style="top:23px">
      <svg class="contact-icon" viewBox="0 0 52 52"><circle cx="26" cy="26" r="26" fill="var(--red)"/><rect x="13" y="17" width="26" height="18" fill="none" stroke="#fff" stroke-width="2.2"/><path d="M13 17 L26 28 L39 17 M13 35 L22 25 M39 35 L30 25" fill="none" stroke="#fff" stroke-width="2.2"/></svg>
      <div class="contact-title">Office 02 5550 0100</div>
      <div class="contact-email">Fuel@terrapetro-example.com.au</div>
    </div>
    <div class="contact" style="top:108px">
      <svg class="contact-icon" viewBox="0 0 52 52"><circle cx="26" cy="26" r="26" fill="var(--red)"/><rect x="13" y="17" width="26" height="18" fill="none" stroke="#fff" stroke-width="2.2"/><path d="M13 17 L26 28 L39 17 M13 35 L22 25 M39 35 L30 25" fill="none" stroke="#fff" stroke-width="2.2"/></svg>
      <div class="contact-title">Marco - 0400 000 001</div>
      <div class="contact-email">mtorrisi@terrapetro-example.com.au</div>
    </div>
    <div class="contact" style="top:193px">
      <svg class="contact-icon" viewBox="0 0 52 52"><circle cx="26" cy="26" r="26" fill="var(--red)"/><rect x="13" y="17" width="26" height="18" fill="none" stroke="#fff" stroke-width="2.2"/><path d="M13 17 L26 28 L39 17 M13 35 L22 25 M39 35 L30 25" fill="none" stroke="#fff" stroke-width="2.2"/></svg>
      <div class="contact-title">Liam - 0400 000 002</div>
      <div class="contact-email">lharcourt@terrapetro-example.com.au</div>
    </div>
    <div class="contact" style="top:277px">
      <svg class="contact-icon" viewBox="0 0 52 52"><circle cx="26" cy="26" r="26" fill="var(--red)"/><rect x="13" y="17" width="26" height="18" fill="none" stroke="#fff" stroke-width="2.2"/><path d="M13 17 L26 28 L39 17 M13 35 L22 25 M39 35 L30 25" fill="none" stroke="#fff" stroke-width="2.2"/></svg>
      <div class="contact-title">Peter - 0400 000 003</div>
      <div class="contact-email">pwinslow@terrapetro-example.com.au</div>
    </div>
  </section>

  <div class="yard-photo" role="img" aria-label="Red above-ground diesel storage tank with a fuel bowser beside a red farm tractor"></div>

  <section class="services">
    <div class="service" style="left:34px">
      <svg width="56" height="64" viewBox="0 0 56 64" aria-hidden="true">
        <rect x="4" y="4" width="30" height="54" rx="3" fill="var(--ink)"/>
        <rect x="10" y="10" width="18" height="14" fill="#fff"/>
        <rect x="0" y="56" width="38" height="6" rx="2" fill="var(--ink)"/>
        <path d="M34 20 L44 26 L44 50 Q44 56 48 56 Q52 56 52 50 L52 24 L46 16" fill="none" stroke="var(--ink)" stroke-width="3.5" stroke-linecap="round"/>
      </svg>
      <div class="service-label" style="left:79px">BULK FUEL<br>DELIVERIES</div>
    </div>
    <div class="service" style="left:294px">
      <svg width="42" height="64" viewBox="0 0 42 64" aria-hidden="true">
        <path d="M21 2 C 14 18, 2 30, 2 43 A19 19 0 0 0 40 43 C 40 30, 28 18, 21 2 Z" fill="var(--red)"/>
        <path d="M13 38 Q 9 50, 18 55" fill="none" stroke="#fff" stroke-width="3" stroke-linecap="round"/>
      </svg>
      <div class="service-label" style="left:68px">OILS &amp;<br>LUBRICANTS</div>
    </div>
    <div class="service" style="left:553px">
      <svg width="76" height="64" viewBox="0 0 76 64" aria-hidden="true">
        <circle cx="14" cy="16" r="9" fill="var(--red)"/>
        <circle cx="62" cy="16" r="9" fill="var(--red)"/>
        <circle cx="38" cy="13" r="12" fill="var(--red)"/>
        <path d="M0 52 Q0 30 14 30 Q24 30 26 38 L26 52 Z" fill="var(--red)"/>
        <path d="M76 52 Q76 30 62 30 Q52 30 50 38 L50 52 Z" fill="var(--red)"/>
        <path d="M16 60 Q16 30 38 30 Q60 30 60 60 Z" fill="var(--red)"/>
      </svg>
      <div class="service-label" style="left:90px">LOCAL FAMILY<br>OWNED BUSINESS</div>
    </div>
  </section>
</main>
</body>
</html>
```